Design a Website in Wordpress for an Australian Health Training Company in Health related courses

We require a WORDPRESS based Website (due to add on's we need to use for third party software) to replace our old site.
We offer national face to face delivery in medical reception, terminology and also administration.
The website will have around 6 pages and the ability to describe our main 6 courses (perhaps on the Courses page this may be tabs opening up to details for example?)
I have attached a previous sample of a Joomla site which was being developed (please do not feel you have to copy this - but I am just giving it as a sample - copying would be boring). But it gives an idea of look/feel and colours which may be suitable. Open to other ideas though.
I will provide some of the content, but would like the ability to finish the content myself.
Images and graphics are important. While a few medical photos re great - don't be tempted to us all pictures of doctors and nurses (although a couple would be good) - these are administrative courses so general corporate, eye catching visionary pictures of people in general are great. A medical type picture is also fine.
THE BOOKING system - will be via an ADD ON which will occur at the end of the project and is supplied by a third party software company (our student management system). This project will include up to 2 hours working with the Tech guys from the third party software to enable the ADD ON. If this ADD ON requires more time, we will pay hourly (although I do not expect it will).
Mostly a female market, many mature aged women target 25-45 yrs. Mixture of medical/health and corporate. Maybe a bit of mums returning to work and corporate inspiration.
It Company
Coded - Design and coding required
5+ page
Must have
- Wordpress
- Great graphics
- Interesting
- professional and clean
- Enquiry section (info Pak)
- Should have a University feel to it - Education
- Pages
- Home Page - About Us - Recruitment -Courses - Class Schedule - Traineeships Queensland Funding - Latest News Blog - Corporate Training- Contact us

```html
<!DOCTYPE html>
<html lang="en">
<head>
<meta charset="utf-8">
<title>Harbourline Health Management – Testimonials</title>
<link rel="stylesheet" href="https://fonts.googleapis.com/css2?family=Open+Sans:ital,wght@0,400;1,400&family=Cabin+Condensed:wght@400&display=swap">
<style>
:root{
  --page-bg:#ffffff;
  --quote-bg:#f7f7f7;
  --accent:#e8a32a;
  --text:#555555;
  --footer-bg:#2b4a6f;
  --footer-bottom:#1b2f55;
  --footer-text:#ffffff;
  --divider:#8ea3bf;
  --rule:#dddddd;
  --field-border:#c9d3df;
  --placeholder:#9a9a9a;
  --send:#7cf57e;
  --reset:#f97c7c;
}
*{box-sizing:border-box;margin:0;padding:0}
html,body{width:1200px;height:657px;overflow:hidden;background:var(--page-bg)}
body{position:relative;font-family:"Open Sans",Arial,sans-serif;color:var(--text)}

.testimonial{position:absolute;left:146px;width:666px;background:var(--quote-bg);border-left:3px solid var(--accent);padding:0 18px;font-style:italic;font-size:12px;line-height:17px}
.testimonial--first{top:-36px;height:100px;padding-top:28px}
.testimonial--second{top:105px;height:110px;padding-top:19px}
.testimonial-author{position:absolute;right:376px;font-size:12px}
.author-first{top:81px}
.author-second{top:233px}
.section-rule{position:absolute;left:146px;top:277px;width:678px;border-top:1px solid var(--rule)}

.site-footer{position:absolute;left:0;top:322px;width:1200px;height:299px;background:var(--footer-bg);border-top:4px solid var(--accent);color:var(--footer-text)}
.enquiry-form .field{position:absolute;background:#fff;border:1px solid var(--field-border);border-radius:2px;font-family:Arial,sans-serif;font-size:9px;color:var(--placeholder);padding:0 8px;display:flex;align-items:center}
.field-first{left:150px;top:28px;width:90px;height:30px}
.field-last{left:248px;top:28px;width:92px;height:30px}
.field-email{left:150px;top:66px;width:190px;height:31px}
.field-subject{left:150px;top:105px;width:190px;height:30px}
.field-message{left:150px;top:143px;width:190px;height:71px;align-items:flex-start!important;padding-top:9px!important}
.button{position:absolute;top:222px;height:27px;border-radius:2px;font-family:Arial,sans-serif;font-size:9px;color:#fff;display:flex;align-items:center;justify-content:center}
.button-send{left:150px;width:90px;background:var(--send)}
.button-reset{left:248px;width:92px;background:var(--reset)}

.footer-divider{position:absolute;border-left:1px dashed var(--divider)}
.divider-a{left:364px;top:25px;height:182px}
.divider-b{left:602px;top:25px;height:115px}
.divider-c{left:840px;top:25px;height:182px}

.footer-column{position:absolute;top:27px}
.footer-heading{font-family:"Cabin Condensed",Arial,sans-serif;font-weight:400;font-size:16px;line-height:20px;margin-bottom:12px}
.footer-text{font-size:12px;line-height:17px}
.col-about{left:384px;width:200px}
.col-posts{left:623px;width:200px}
.col-testimony{left:860px;width:200px}
.post-list{list-style:none;font-size:12px;line-height:17px}
.post-list li{display:flex;align-items:center;gap:7px}
.post-list svg{flex:none}

.footer-bottom{position:absolute;left:0;top:621px;width:1200px;height:36px;background:var(--footer-bottom);color:var(--footer-text);font-size:12px;text-align:center;line-height:24px;padding-top:9px}
.back-to-top{position:absolute;left:1142px;top:613px;width:37px;height:32px;background:var(--accent);display:flex;align-items:center;justify-content:center}
</style>
</head>
<body>
  <blockquote class="testimonial testimonial--first">“I have just completed my 6 month probation period at Kingsmere Hospital and loving it. It was my first medical job I applied for literally 1-2 weeks after I finished the course. Thanks to you, Rosa, and all the other teachers and staff at Harbourline Health Management.”</blockquote>
  <p class="testimonial-author author-first">Tessa</p>

  <blockquote class="testimonial testimonial--second">I completed the course on Feb 13th. Loved it. The trainers, Lena and Kate were excellent in their delivery and knowledge. I want to say a huge thank you for the course and knowledge I came away with. I have secured a fantastic job after my first application! Such good value for money too! I would highly recommend it. I’m a mature age person so it’s never too late to up -skill yourself to get what you deserve!</blockquote>
  <p class="testimonial-author author-second">Joan Bradley</p>
  <div class="section-rule"></div>

  <footer class="site-footer">
    <div class="enquiry-form">
      <div class="field field-first">First Name</div>
      <div class="field field-last">Last Name</div>
      <div class="field field-email">Email</div>
      <div class="field field-subject">Subject</div>
      <div class="field field-message">Message</div>
      <div class="button button-send">SEND</div>
      <div class="button button-reset">RESET</div>
    </div>

    <div class="footer-divider divider-a"></div>
    <div class="footer-divider divider-b"></div>
    <div class="footer-divider divider-c"></div>

    <section class="footer-column col-about">
      <h3 class="footer-heading">About Harbourline</h3>
      <p class="footer-text">Harbourline Health Management started business in February 1999 primarily as a Medical and Dental Recruitment Company. As Harbourline evolved, services expanded to a comprehensive IT Division servicing doctors and dentists in medical software and IT solutions.</p>
    </section>

    <section class="footer-column col-posts">
      <h3 class="footer-heading">Recent Posts</h3>
      <ul class="post-list">
        <li><svg width="7" height="8" viewBox="0 0 7 8"><path d="M0 0l3 4-3 4h2l3-4-3-4zM3 0l3 4-3 4h1l3-4-3-4z" fill="#e8a32a"/></svg>Harbourline Institute</li>
        <li><svg width="7" height="8" viewBox="0 0 7 8"><path d="M0 0l3 4-3 4h2l3-4-3-4zM3 0l3 4-3 4h1l3-4-3-4z" fill="#e8a32a"/></svg>Graduate</li>
        <li><svg width="7" height="8" viewBox="0 0 7 8"><path d="M0 0l3 4-3 4h2l3-4-3-4zM3 0l3 4-3 4h1l3-4-3-4z" fill="#e8a32a"/></svg>Welcome To Harbourline</li>
        <li><svg width="7" height="8" viewBox="0 0 7 8"><path d="M0 0l3 4-3 4h2l3-4-3-4zM3 0l3 4-3 4h1l3-4-3-4z" fill="#e8a32a"/></svg>Admission Open</li>
      </ul>
    </section>

    <section class="footer-column col-testimony">
      <h3 class="footer-heading">Testimony</h3>
      <p class="footer-text">“I have just completed my 6 month probation period at Kingsmere Hospital and loving it. It was my first medical job I applied for literally 1-2 weeks after I finished the course. Thanks to you, Rosa, and all the other teachers and staff at Harbourline Health Management.” -Tessa</p>
    </section>
  </footer>

  <div class="footer-bottom">Copyright. All rights reserved.</div>

  <div class="back-to-top" aria-label="Back to top">
    <svg width="18" height="12" viewBox="0 0 18 12"><path d="M2 10l7-7 7 7" fill="none" stroke="#1b2f55" stroke-width="3"/></svg>
  </div>
</body>
</html>
```